Brambel Logging Business Card Design Project

We need a new company business card. We provide professional timber harvesting (logging) and forest management services. I'm open to any creative design. Most company caps and shirts are navy blue and Light grey. Logo does not necessarily have to contain those colors. Logo containing picture of logging equipment, log truck, trees, or logs are acceptable. Be creative. Final logo should communicate our company's pride and professionalism in the East Texas Timber Industry.
Updates

Target Market(s)

Timber owners, sawmills, and forestry professionals

Industry/Entity Type

Business

Requirements
Must have
• Must have Contact Info.
Phone: 936-402-5817
address: PO Box 8462
New Waverly, Tx 77358
www.mbrambellogging.example
mbrambellogging@mailbox.example
Owner: Marv Brambel

Or design must leave room for this info.

```html
<!DOCTYPE html>
<html lang="en">
<head>
<meta charset="utf-8">
<title>Brambel Logging – Business Card</title>
<link rel="stylesheet" href="https://fonts.googleapis.com/css2?family=Michroma&display=swap">
<style>
  :root {
    --card-white: #ffffff;
    --brand-red: #e0242b;
    --brand-red-deep: #c81d23;
    --charcoal: #2f2f31;
    --ink: #2a2a2a;
    --on-red: #ffffff;
    --page: #e9e9e9;
  }
  * { margin: 0; padding: 0; box-sizing: border-box; }
  html, body {
    width: 1200px; height: 771px; overflow: hidden;
    background: var(--page);
  }
  .card {
    position: relative;
    width: 1200px; height: 771px;
    background: var(--card-white);
    overflow: hidden;
    font-family: "Michroma", sans-serif;
  }
  .card__waves { position: absolute; inset: 0; width: 100%; height: 100%; }
  .wave--stripe { fill: var(--charcoal); }
  .wave--band { fill: url(#bandGradient); }

  .brand {
    position: absolute;
    left: 600px; top: 200px;
    display: flex; align-items: center; gap: 28px;
  }
  .brand__name {
    display: block;
    width: 350px;
    color: var(--ink);
    font-size: 42px;
    letter-spacing: 1px;
    text-transform: uppercase;
    line-height: 1.15;
  }
  .brand__mark {
    flex: none;
    width: 40px; height: 40px;
    background: var(--brand-red);
  }

  .contact {
    position: absolute;
    left: 0; top: 480px;
    width: 1200px;
    color: var(--on-red);
  }
  .contact__person {
    position: absolute;
    right: 640px; top: 0;
    text-align: right;
    white-space: nowrap;
  }
  .contact__name { font-size: 26px; letter-spacing: 2px; text-transform: uppercase; }
  .contact__title { font-size: 16px; letter-spacing: 2px; margin-top: 8px; }
  .contact__address { font-size: 18px; letter-spacing: 2px; margin-top: 22px; line-height: 1.6; }
  .contact__divider {
    position: absolute;
    left: 585px; top: 0;
    width: 2px; height: 230px;
    background: var(--on-red);
    opacity: .8;
  }
  .contact__lines {
    position: absolute;
    left: 610px; top: 0;
    list-style: none;
  }
  .contact__line {
    display: flex; align-items: center; gap: 14px;
    font-size: 19px; letter-spacing: 2px;
    height: 44px;
    white-space: nowrap;
  }
  .contact__icon { width: 26px; height: 26px; flex: none; }
  .icon-disc { fill: var(--on-red); }
  .icon-glyph { fill: var(--brand-red); stroke: var(--brand-red); }
</style>
</head>
<body>
<main class="card">
  <svg class="card__waves" viewBox="0 0 1200 771" aria-hidden="true">
    <defs>
      <linearGradient id="bandGradient" x1="0" y1="0" x2="1" y2="1">
        <stop offset="0" stop-color="#e8282f"/>
        <stop offset="1" stop-color="#c81d23"/>
      </linearGradient>
    </defs>
    <path class="wave--stripe" d="M0,285 C330,275 720,500 1200,500 L1200,560 C720,560 330,340 0,345 Z"/>
    <path class="wave--band" d="M0,330 C330,320 720,540 1200,545 L1200,771 L0,771 Z"/>
  </svg>

  <header class="brand">
    <span class="brand__name">Brambel Logging</span>
    <span class="brand__mark"></span>
  </header>

  <section class="contact">
    <div class="contact__person">
      <p class="contact__name">Marv Brambel</p>
      <p class="contact__title">Owner / C.E.O</p>
      <p class="contact__address">PO Box 0142<br>Fernhollow, Tx 00000</p>
    </div>
    <span class="contact__divider"></span>
    <ul class="contact__lines">
      <li class="contact__line">
        <svg class="contact__icon" viewBox="0 0 26 26"><circle class="icon-disc" cx="13" cy="13" r="13"/><path class="icon-glyph" stroke="none" d="M8 7.5l3 -1 2 4 -2 1.5c.8 1.8 2.2 3.2 4 4l1.5-2 4 2-1 3c-6 .5-11.5-5-11.5-11.5z"/></svg>
        555-201-4817
      </li>
      <li class="contact__line">
        <svg class="contact__icon" viewBox="0 0 26 26"><circle class="icon-disc" cx="13" cy="13" r="13"/><rect class="icon-glyph" stroke="none" x="9" y="5.5" width="8" height="15" rx="1.5"/><rect fill="#fff" x="10.5" y="7.5" width="5" height="9"/></svg>
        555-201-4819
      </li>
      <li class="contact__line">
        <svg class="contact__icon" viewBox="0 0 26 26"><circle class="icon-disc" cx="13" cy="13" r="13"/><rect class="icon-glyph" stroke="none" x="6" y="11" width="14" height="9" rx="1"/><rect class="icon-glyph" stroke="none" x="9" y="6" width="8" height="6"/><rect fill="#fff" x="9" y="14" width="8" height="2"/></svg>
        555-201-4820
      </li>
      <li class="contact__line">
        <svg class="contact__icon" viewBox="0 0 26 26"><circle class="icon-disc" cx="13" cy="13" r="13"/><rect class="icon-glyph" fill="none" stroke-width="1.8" x="6" y="8" width="14" height="10" rx="1"/><path class="icon-glyph" fill="none" stroke-width="1.8" d="M6 8l7 6 7-6"/></svg>
        mbrambellogging@mailbox.example
      </li>
      <li class="contact__line">
        <svg class="contact__icon" viewBox="0 0 26 26"><circle class="icon-disc" cx="13" cy="13" r="13"/><g class="icon-glyph" fill="none" stroke-width="1.6"><circle cx="13" cy="13" r="7"/><ellipse cx="13" cy="13" rx="3" ry="7"/><path d="M6 13h14"/></g></svg>
        www.mbrambellogging.example
      </li>
    </ul>
  </section>
</main>
</body>
</html>
```